Winterization checkup email mail out

I have a handyman business and I want to design an email that will be sent out every month to our clients, so we will need a start design and are doing a home winterization package for residential clients, we are going to sell our "winterization package consultation" for $1 we will assess the clients house for what needs to be done every year for prevention, I want to have a cartoon "ish" look to it and round circles "buttons" with the sign for plumbing, electrical, freezing, cold and etc and a slogan for the campaign. I will be uploading our company logo and name.
Updates

I also uploaded pictures of our van and there is also a list of what are we looking to get it done in the "estimate", we would like to incorporate our van pictures in the design as well. Here is a description of the items we are going to be selling and that need to be incorporated into the design: Winterization checkup Is your house prepped for winter? Get started with a winterization checkup before the cold hits. What we look for: Window exterior sealing Drafts coming in from power outlets, electrical, gas and water lines Identify energy-inefficient red flags such as in-window air conditioning units left Gutter: check condition, and/or for caps or gutter protection Chimney, make sure is clean and shut is closed. Chimney and cap Vent cover condition, and attachment to chimney or vent pipes. Plumbing shut off valves Loose siding, flashing, and trim Recommendations for preventive measures, where applicable: Offer suggestions to homeowner about different new products that can help their house be more energy efficient and sealed for winter as of: Spray insulation, that can be applied to the walls to prevent cold climate. (example of ) Recommend preventive measures such as roof cables to prevent snow build up of ice dams. Inspect and reinforce railings (Deck, exterior stairs) AVOID: Expensive plumbing repairs from frozen pipes High energy bills from not properly sealed insulated doors and windows Hazards from dangerous falling gutter ice dams

Industry/Entity Type

Handyman

Font styles to use
Serif

Requirements
Must have
• I am picturing a cartoon "ish" house in the back with most common winter in USA problems in the east coast, frozen pipes, ventilation and so on, here are some samples of the checklist:
• Winterization checkup
• Is your house prepped for winter? Get started with a winterization checkup before the cold hits.
• AVOID:
• Expensive plumbing repairs from frozen pipes
• High energy bills from not properly sealed insulated doors and windows
• Hazards from dangerous falling gutter ice dams
• What we look for:
• Window exterior sealing
• Drafts coming in from power outlets, electrical, gas and water lines
• Identify energy-inefficient red flags such as in-window air conditioning units left
• Gutter: check condition, and/or for caps or gutter protection
• Chimney, make sure is clean and shut is closed.
• Chimney and cap
• Vent cover condition, and attachment to chimney or vent pipes.
• Plumbing shut off valves
• Loose siding, flashing, and trim
• Recommendations for preventive measures, where applicable:
• Offer suggestions to homeowner about different new products that can help their house be more energy efficient and sealed for winter as of:
• Spray insulation, that can be applied to the walls to prevent cold climate. (example of )
• Recommend preventive measures such as roof cables to prevent snow build up of ice dams.
• Inspect and reinforce railings (Deck, exterior stairs)
Nice to have
• Smart use of the company logo and colors, since this is going to be a montly email, I would like to have aspects that can be easily edited so we can re use the same email to highlithg other material as well within the same Fall, winter Theme

```html
<!DOCTYPE html>
<html lang="en">
<head>
<meta charset="utf-8">
<title>Fixwell Handyman Services – Winterization Package</title>
<link rel="stylesheet" href="https://fonts.googleapis.com/css2?family=Jost:wght@400;500;600;700&family=Oswald:wght@500;600;700&display=swap">
<style>
  :root {
    --page-bg: #d0d1c7;
    --card-bg: #ffffff;
    --ink: #111111;
    --body-ink: #555555;
    --muted-ink: #444444;
    --brand-red: #e8202a;
    --brand-yellow: #f6b41e;
    --brand-orange: #fba52c;
    --sky: #88c6d6;
    --hero-band: #c3dbe3;
    --rule: #d9d9d9;
    --tile-orange: #f8a93a;
    --tile-navy: #47668c;
    --tile-olive: #889c63;
  }
  * { box-sizing: border-box; margin: 0; padding: 0; }
  html, body { width: 1200px; height: 2542px; overflow: hidden; }
  body {
    position: relative;
    background: var(--page-bg);
    font-family: "Jost", "Helvetica Neue", Arial, sans-serif;
    color: var(--ink);
  }
  .preheader {
    position: absolute; top: 88px; left: 0; width: 1200px;
    text-align: center; font-family: Arial, Helvetica, sans-serif;
    font-size: 19px; line-height: 26px; color: #555;
  }
  .preheader a { color: var(--brand-red); text-decoration: underline; }

  .email-card {
    position: absolute; left: 231px; top: 173px; width: 740px; height: 2166px;
    background: var(--card-bg); border-radius: 12px; overflow: hidden;
    box-shadow: 0 6px 40px rgba(0,0,0,0.12);
  }
  .abs { position: absolute; }

  /* brand */
  .brand { display: flex; align-items: center; gap: 12px; }
  .brand-dot { border-radius: 50%; background: var(--brand-red); }
  .brand-name { font-weight: 700; color: var(--ink); letter-spacing: -0.5px; }
  .brand--header { left: 0; top: 0; width: 740px; height: 152px; justify-content: center; }
  .brand--header .brand-dot { width: 54px; height: 54px; }
  .brand--header .brand-name { font-size: 62px; line-height: 1; }

  /* hero */
  .hero-band { left: 0; top: 152px; width: 740px; height: 634px; background: var(--hero-band); }
  .hero-art {
    left: 0; top: 152px; width: 740px; height: 370px;
    background: linear-gradient(180deg, var(--sky) 0%, #a9d6e2 55%, #eaf4f7 78%, #dfeef3 100%);
  }
  .hero-title {
    left: 0; top: 570px; width: 740px; text-align: center;
    font-family: "Oswald", "Arial Narrow", sans-serif; font-weight: 600;
    font-size: 40px; line-height: 50px; color: var(--ink); letter-spacing: 0.3px;
  }
  .hero-sub {
    left: 0; top: 625px; width: 740px; text-align: center;
    font-size: 20px; font-weight: 600; color: var(--ink);
  }
  .hero-sub .accent { color: var(--brand-red); }

  .pill {
    display: flex; align-items: center; justify-content: center;
    border-radius: 40px; font-weight: 600; text-decoration: none;
  }
  .pill--primary {
    left: 145px; top: 674px; width: 438px; height: 56px;
    background: var(--brand-red); color: #fff; font-size: 23px;
    box-shadow: 0 0 0 5px #fff;
  }

  /* section headings */
  .section-heading {
    left: 31px; width: 678px; display: flex; align-items: center; gap: 20px;
    font-size: 34px; font-weight: 600; color: var(--ink); white-space: nowrap;
  }
  .section-heading::before, .section-heading::after {
    content: ""; flex: 1; height: 1px; background: var(--rule);
  }
  .services-heading { top: 850px; }
  .package-heading { top: 1332px; }

  .services-intro {
    left: 31px; top: 900px; width: 678px; text-align: center;
    font-size: 21px; line-height: 29px; color: var(--body-ink);
  }

  .service { top: 998px; width: 132px; text-align: center; }
  .service-tile { width: 112px; height: 112px; margin: 0 auto; }
  .service-tile--orange { background: var(--tile-orange); }
  .service-tile--navy { background: var(--tile-navy); }
  .service-tile--olive { background: var(--tile-olive); }
  .service-label {
    margin-top: 13px; font-size: 17px; line-height: 19px; font-weight: 600; color: var(--muted-ink);
  }
  .badge-new {
    top: -38px; width: 50px; height: 50px; border-radius: 50%;
    background: var(--brand-red); color: #fff; font-size: 16px; font-weight: 700;
    display: flex; align-items: center; justify-content: center; z-index: 2;
  }
  .pill--outline {
    left: 230px; top: 1208px; width: 280px; height: 56px;
    border: 2px solid #8a8a8a; color: #444; font-size: 18px; background: #fff;
  }

  /* package */
  .package-copy {
    left: 30px; top: 1434px; width: 465px;
    font-size: 20px; line-height: 33px; color: var(--body-ink);
  }
  .offer-banner { left: 30px; top: 1691px; width: 682px; height: 150px; }
  .offer-text { left: 36px; top: 50px; color: var(--ink); }
  .offer-line1 {
    font-family: "Oswald", "Arial Narrow", sans-serif; font-weight: 500;
    font-size: 24px; line-height: 30px; color: #1a1a1a;
  }
  .offer-line2 {
    font-family: "Oswald", "Arial Narrow", sans-serif; font-weight: 600;
    font-size: 31px; line-height: 38px; color: #fff;
  }
  .offer-line2 .accent { color: var(--brand-red); }
  .handyman-art {
    left: 498px; top: 1412px; width: 220px; height: 432px;
    background: linear-gradient(180deg, #f7a52a 0%, #f3c9a8 22%, #2f62a8 45%, #24508f 75%, #f3b320 100%);
    border-radius: 90px 90px 0 0;
  }
  .price-bubble {
    left: 520px; top: 1716px; width: 142px; height: 112px; border-radius: 56px;
    background: #fff; border: 4px solid var(--brand-red);
    display: flex; align-items: center; justify-content: center;
    font-family: "Oswald", "Arial Narrow", sans-serif; font-weight: 700;
    font-size: 64px; color: var(--brand-red);
  }
  .pill--buy {
    left: 264px; top: 1873px; width: 210px; height: 56px;
    background: var(--brand-red); color: #fff; font-size: 22px;
    box-shadow: 0 0 0 5px var(--brand-yellow);
  }

  /* footer */
  .footer-rule { left: 31px; top: 1997px; width: 678px; height: 1px; background: var(--rule); }
  .brand--footer { left: 31px; top: 2030px; gap: 8px; }
  .brand--footer .brand-dot { width: 26px; height: 26px; }
  .brand--footer .brand-name { font-size: 32px; line-height: 1; }
  .footer-url { left: 31px; top: 2082px; font-size: 20px; color: var(--body-ink); }
  .follow-title { left: 473px; top: 2028px; width: 230px; text-align: left; font-size: 20px; font-weight: 600; color: var(--muted-ink); }
  .social-list { left: 476px; top: 2073px; display: flex; gap: 12px; list-style: none; }
  .social-list li {
    width: 49px; height: 49px; border-radius: 50%; background: var(--brand-red);
    box-shadow: 0 0 0 4px #fff, 0 0 0 6px #d7d7d7;
  }
</style>
</head>
<body>
  <p class="preheader">Is this email not displaying correctly?<br><a href="#">View it in your browser.</a></p>

  <main class="email-card">
    <header class="abs brand brand--header">
      <span class="brand-dot"></span><span class="brand-name">fixwell</span>
    </header>

    <section class="hero">
      <div class="abs hero-band"></div>
      <div class="abs hero-art" role="img" aria-label="Cartoon house wrapped in a scarf and earmuffs in a snowy landscape with pine trees"></div>
      <h1 class="abs hero-title">IS YOUR HOME PREPARE FOR WINTER?</h1>
      <p class="abs hero-sub"><span class="accent">If not</span> , buy Our recent Package for $1</p>
      <a class="abs pill pill--primary" href="#">Winterizatin Package Consultation</a>
    </section>

    <section class="services">
      <h2 class="abs section-heading services-heading">Our Services</h2>
      <p class="abs services-intro">We will assess the clients house for what needs to be done every year for prevention like&nbsp; frozen pipes, ventilation and so on.</p>

      <div class="abs service" style="left:20px">
        <div class="service-tile service-tile--orange" role="img" aria-label="Illustration of weather stripping being painted on a window"></div>
        <p class="service-label">Invest in weather stripping</p>
      </div>
      <div class="abs service" style="left:162px">
        <span class="abs badge-new" style="left:41px">New</span>
        <div class="service-tile service-tile--navy" role="img" aria-label="Illustration of a worker cleaning a gutter"></div>
        <p class="service-label">Clean your gutters</p>
      </div>
      <div class="abs service" style="left:306px">
        <div class="service-tile service-tile--olive" role="img" aria-label="Illustration of a roofer with a hammer"></div>
        <p class="service-label">Evaluate your roof to prevent ice dams</p>
      </div>
      <div class="abs service" style="left:449px">
        <div class="service-tile service-tile--orange" role="img" aria-label="Illustration of a plumber fixing a pipe"></div>
        <p class="service-label">Protect pipes from freezing</p>
      </div>
      <div class="abs service" style="left:591px">
        <span class="abs badge-new" style="left:41px">New</span>
        <div class="service-tile service-tile--olive" role="img" aria-label="Illustration of a worker with basic supplies"></div>
        <p class="service-label">Stock up on basics</p>
      </div>

      <a class="abs pill pill--outline" href="#">Watch Details for More</a>
    </section>

    <section class="package">
      <h2 class="abs section-heading package-heading">Our Package Details</h2>
      <p class="abs package-copy">Our&nbsp; services based in millbrook, pa serving cedar county , alder county, willow county, aspen county. We are going to start home winterization package for residential clients name "winterization package consultation" for $1. we will assess the clients house for what needs to be done every year for prevention .</p>

      <div class="abs offer-banner">
        <svg width="682" height="150" viewBox="0 0 682 150" aria-hidden="true">
          <polygon points="0,0 330,25 682,12 682,150 0,150" fill="#fba52c"/>
          <polygon points="0,0 330,25 0,42" fill="#e8202a"/>
        </svg>
        <div class="abs offer-text">
          <p class="offer-line1">Purchase Our Winterization</p>
          <p class="offer-line2">“PACKAGE CONSULTATION” for <span class="accent">$1</span></p>
        </div>
      </div>
      <div class="abs handyman-art" role="img" aria-label="Cartoon handyman in a hard hat carrying a coil of cable"></div>
      <div class="abs price-bubble">$1</div>

      <a class="abs pill pill--buy" href="#">Buy Now</a>
    </section>

    <footer>
      <div class="abs footer-rule"></div>
      <div class="abs brand brand--footer"><span class="brand-dot"></span><span class="brand-name">fixwell</span></div>
      <p class="abs footer-url">https://fixwellhandy.example/</p>
      <p class="abs follow-title">Please Follow us on</p>
      <ul class="abs social-list" aria-label="Social channels">
        <li aria-label="Social channel 1"></li>
        <li aria-label="Social channel 2"></li>
        <li aria-label="Social channel 3"></li>
        <li aria-label="Social channel 4"></li>
      </ul>
    </footer>
  </main>
</body>
</html>
```